Dr Mira Thalen, Orthopaedic Hand Surgeon

I am an orthopaedic hand surgeon and need business cards that reflect the surgery I do. I operate on bones, ligaments, tendons, and soft tissues. I can do microsurgery (surgery under an operating microscope) - including connecting ends of cut nerves and arteries in the fingers together. As an orthopaedic surgeon, I also fix fractures and manage orthopaedic trauma in the rest of the body. I favour black as a colour, and have some pictures of hand X-rays that you can use in the design, if you think that would look good (feel free to crop).
Updates

Hi all. Thank you for all your submissions so far. Please note that I have updated my project brief. I would like to emphasise that use of the logos that I have provided is optional, and if used, I would very much prefer the logo not to dominate the card, but add to the overall aesthetic of the card. Warm regards, Mira

Target Market(s)

Referring medical practitioners, hand therapists, patients

Industry/Entity Type

Healthcare

Contact Information for Business Card

Dr Mira Thalen
Orthopaedic Hand Surgeon
MBBS BSc (Med), MIntPH (Merit), FCWES (Ortho), FUPelV

Font styles to use
Serif

Colors

Designer to choose colors to be used in the design.

Requirements
Must have
• Space for:
• 2 addresses (a PO Box Address and a consulting suite address) - to be confirmed
• 1 phone number - to be confirmed
Nice to have
• Please choose one of the FCWES logos (I included 3 - colour, black reverse, and greyscale); if you include this in the design, IT SHOULD NOT DOMINATE THE CARD, but be smaller and more discreet.
• I have also attached the FUPelV logo (colour and greyscale); if you choose to include this in the design, IT SHOULD NOT DOMINATE THE CARD, but be smaller and more discreet.
• I would love to be able to update details on the card as time goes on, and thus would like to own the template for the card as well.
• Also I would love discussion with regard to any changes on the card, if I am not completely happy with the design, and would like to discuss things such as ease of printing, finish on the cards (matte, polish) etc.
Should not have
• I don't like the card to look too crowded

```html
<!DOCTYPE html>
<html lang="en">
<head>
<meta charset="utf-8">
<title>Dr Mira Thalen – Business Card</title>
<link rel="stylesheet" href="https://fonts.googleapis.com/css2?family=Roboto:wght@400;500&family=Roboto+Condensed:wght@700&display=swap">
<style>
  :root {
    --backdrop: #e6e6e6;
    --card-light: #f6f6f6;
    --card-dark: #1c1c1c;
    --ink-strong: #1e1e1e;
    --ink-mid: #6e6e6e;
    --ink-soft: #5a5a5a;
    --rule: #9a9a9a;
    --reverse: #ffffff;
  }
  * { margin: 0; padding: 0; box-sizing: border-box; }
  html, body { width: 1200px; height: 960px; overflow: hidden; }
  body {
    background: var(--backdrop);
    font-family: "Roboto", Arial, sans-serif;
    position: relative;
  }
  .card { position: absolute; width: 601px; height: 334px; }
  .card--front { left: 302px; top: 129px; background: var(--card-light); color: var(--ink-soft); }
  .card--back { left: 299px; top: 488px; height: 342px; background: var(--card-dark); color: var(--reverse); }

  .assoc-mark {
    position: absolute; left: 34px; top: 58px;
    font-size: 14px; color: var(--ink-mid); letter-spacing: 0.5px;
  }
  .college-mark { position: absolute; right: 36px; top: 30px; display: flex; align-items: center; gap: 8px; }
  .college-mark__square { width: 16px; height: 16px; background: var(--ink-mid); }
  .college-mark__name { font-size: 30px; color: var(--ink-mid); line-height: 1; }
  .college-mark__tagline {
    position: absolute; right: 36px; top: 56px; text-align: right;
    font-size: 9.5px; line-height: 1.35; color: var(--ink-soft);
  }

  .identity { position: absolute; left: 32px; top: 140px; }
  .identity__name {
    font-family: "Roboto Condensed", "Arial Narrow", sans-serif;
    font-weight: 700; font-size: 20px; color: var(--ink-strong); letter-spacing: 0.2px;
  }
  .identity__role { font-size: 15px; font-weight: 500; color: var(--ink-mid); margin-top: 2px; }
  .identity__credentials { font-size: 13px; line-height: 17px; color: var(--ink-mid); margin-top: 3px; }

  .divider { position: absolute; left: 32px; right: 37px; top: 226px; border-top: 1px solid var(--rule); }

  .addresses { position: absolute; left: 33px; top: 239px; font-size: 14px; line-height: 18px; }
  .addresses__item + .addresses__item { margin-top: 4px; }

  .contact { position: absolute; right: 37px; top: 257px; font-size: 14px; line-height: 19.5px; list-style: none; }
  .contact__item { display: flex; align-items: center; justify-content: flex-end; gap: 9px; }
  .contact__icon { width: 13px; height: 13px; fill: var(--ink-strong); }

  .back-mark {
    position: absolute; left: 0; right: 0; top: 128px;
    display: flex; justify-content: center; align-items: center; gap: 12px;
  }
  .back-mark__square { width: 22px; height: 22px; background: var(--reverse); }
  .back-mark__name { font-size: 40px; letter-spacing: 3px; }
  .back-url {
    position: absolute; left: 0; right: 0; top: 283px; text-align: center;
    font-size: 14px; letter-spacing: 3.2px;
  }
</style>
</head>
<body>
  <section class="card card--front">
    <div class="assoc-mark">FUPelV</div>

    <div class="college-mark">
      <span class="college-mark__square"></span>
      <span class="college-mark__name">FCWES</span>
    </div>
    <p class="college-mark__tagline">Fellow of the<br>College of Wrist &amp; Extremity Surgeons</p>

    <div class="identity">
      <h1 class="identity__name">DR MIRA THALEN</h1>
      <p class="identity__role">Orthopaedic Hand Surgeon</p>
      <p class="identity__credentials">MBBS BSc (Med), MIntPH (Merit)<br>FCWES (Ortho), FUPelV</p>
    </div>

    <div class="divider"></div>

    <div class="addresses">
      <p class="addresses__item">412 Larkfield Road<br>Hollow Bay, Norvale 20417</p>
      <p class="addresses__item">PO Box 318<br>Hollow Bay, Norvale 20419</p>
    </div>

    <ul class="contact">
      <li class="contact__item">555 014 2290
        <svg class="contact__icon" viewBox="0 0 16 16" aria-hidden="true"><path d="M3.6 1.2 5.8 3.4c.4.4.4 1 0 1.4L4.7 5.9c.9 2 2.5 3.6 4.5 4.5l1.1-1.1c.4-.4 1-.4 1.4 0l2.2 2.2c.4.4.4 1 0 1.4l-1.2 1.2C11.6 15.2 1 6.6.9 2.3L2.2 1.2c.4-.4 1-.4 1.4 0z"/></svg>
      </li>
      <li class="contact__item">mira@fcwes.com
        <svg class="contact__icon" viewBox="0 0 16 16" aria-hidden="true"><path d="M1 3h14v1.2L8 9 1 4.2z"/><path d="M1 5.6 8 10.4l7-4.8V13H1z"/></svg>
      </li>
      <li class="contact__item">www.fcwes.com
        <svg class="contact__icon" viewBox="0 0 16 16" aria-hidden="true"><circle cx="8" cy="8" r="7"/><path d="M5 4c1 .5 2 .3 2.5 1.3S6 7 6.8 8 9 8.6 9 10s-1 2-.8 3.2C6 12 5.5 10 4.5 9S3 6 5 4zM10 3.5c1 0 2.5 1 2.8 2.3-.8 0-1.5-.4-2-.9z" fill="var(--card-light)"/></svg>
      </li>
    </ul>
  </section>

  <section class="card card--back">
    <div class="back-mark">
      <span class="back-mark__square"></span>
      <span class="back-mark__name">FCWES</span>
    </div>
    <p class="back-url">WWW.FCWES.COM</p>
  </section>
</body>
</html>
```